Broschüre für eine Trainingsakademie
Zielgruppe
Ich möchte eine Broschüre zu meinem Unternehmen und meinen Angeboten schöner Design haben.
Ich bin Trainer/ Coach für moderne Personalstrategien insbesondere für die Personalgewinnung, Mitarbeiterbindung und -entwicklung. Zudem biete ich Trainings und Coachings für Mitarbeiter und Führungskräfte an. Zum Beispiel zu Themen wie gesunde Führung, Stressmanagement, Resilienz usw.
Meine Zielgruppe sind vor allem mittelständische Unternehmen oder junge aufstrebende StartUps, die ich beim Aufbau von Personalstrukturen unterstütze.
Aufgabenstellung
Mein Logo und die Farben sollen entsprechend berücksichtigt werden. Ein Entwurf für die Broschüre besteht bereits. Das ist allerdings nur meine Idee, als Laie. Ich hätte hier gern professionelle Ideen, so dass die Broschüre professionell und ansprechend wirkt.
Bilder habe ich eigentlich - diese finden sich auch auf meiner Homepage. Allerdings bin ich gerade auch beim Deckblatt offen. Auch für andere Gestaltungsvorschläge.

```html
<!DOCTYPE html>
<html lang="de">
<head>
<meta charset="utf-8">
<title>Die Trainingsakademie – Broschüre</title>
<link rel="stylesheet" href="https://fonts.googleapis.com/css2?family=Arimo:wght@400;700&display=swap">
<style>
  :root {
    --ink: #1d1d1b;
    --brand: #544a7c;
    --brand-soft: #9d97b5;
    --column: #9a91b1;
    --column-light: #b3abc8;
    --cloud-light: #cbc6d8;
    --cloud-dark: #5a4f80;
    --chevron-grey: #cbc7d6;
    --chevron-lilac: #ddd6ee;
    --paper: #ffffff;
  }
  html, body {
    margin: 0;
    padding: 0;
    overflow: hidden;
    background: var(--paper);
  }
  .cover {
    position: relative;
    width: 1200px;
    height: 846px;
    overflow: hidden;
    background: var(--paper);
    font-family: "Arimo", Arial, sans-serif;
  }
  .cover-art {
    position: absolute;
    inset: 0;
  }
  .frame-line { stroke: var(--brand); stroke-width: 2; fill: none; }
  .leader { stroke: var(--ink); stroke-width: 3; stroke-dasharray: 0.1 5.6; stroke-linecap: round; fill: none; }
  .title-article, .title-for { fill: var(--brand-soft); font-weight: 700; }
  .title-main { fill: var(--brand); font-weight: 700; }
  .topic { fill: var(--ink); font-weight: 400; }
  .brand-name { fill: var(--brand); font-weight: 700; }
</style>
</head>
<body>
<main class="cover">
  <svg class="cover-art" width="1200" height="846" viewBox="0 0 1200 846" xmlns="http://www.w3.org/2000/svg">
    <defs>
      <linearGradient id="chevron-fade" x1="0" y1="0" x2="1" y2="0">
        <stop offset="0" stop-color="#f4f2f8"/>
        <stop offset="1" stop-color="var(--chevron-lilac)"/>
      </linearGradient>
      <linearGradient id="cloud-fill" x1="0" y1="0" x2="0" y2="1">
        <stop offset="0" stop-color="var(--cloud-light)"/>
        <stop offset="0.55" stop-color="#a39cbb"/>
        <stop offset="1" stop-color="var(--cloud-dark)"/>
      </linearGradient>
      <linearGradient id="column-fill" x1="0" y1="0" x2="0" y2="1">
        <stop offset="0" stop-color="var(--column)"/>
        <stop offset="1" stop-color="var(--column-light)"/>
      </linearGradient>
      <linearGradient id="city-fill" x1="0" y1="0" x2="0" y2="1">
        <stop offset="0" stop-color="#8f86a8"/>
        <stop offset="0.5" stop-color="#9fd6e0"/>
        <stop offset="1" stop-color="#9a91b1"/>
      </linearGradient>
    </defs>

    <!-- decorative chevrons -->
    <g class="chevrons">
      <polygon points="62,0 125,0 243,116 200,158 120,78" fill="var(--chevron-grey)"/>
      <polygon points="0,0 45,0 265,224 160,340 20,340 140,224 0,84" fill="url(#chevron-fade)" opacity="0.9"/>
      <polygon points="0,70 112,184 0,296" fill="#f7f6fa"/>
      <polygon points="0,165 50,212 0,262" fill="var(--paper)"/>
    </g>

    <!-- title frame -->
    <line class="frame-line" x1="0" y1="342" x2="716" y2="342"/>
    <line class="frame-line" x1="128" y1="281" x2="1200" y2="281"/>
    <line class="frame-line" x1="128" y1="281" x2="128" y2="363"/>
    <line class="frame-line" x1="716" y1="261" x2="716" y2="342"/>

    <text class="title-article" x="73" y="308" font-size="31">die</text>
    <text class="title-main" x="132" y="333" font-size="54" textLength="579" lengthAdjust="spacingAndGlyphs">TRAININGSAKADEMIE</text>
    <text class="title-for" x="726" y="342" font-size="28">für</text>

    <!-- topics -->
    <text class="topic" x="502" y="422" font-size="35" text-anchor="end" textLength="370" lengthAdjust="spacingAndGlyphs">PERSONALSTRATEGIE</text>
    <text class="topic" x="502" y="491" font-size="35" text-anchor="end" textLength="426" lengthAdjust="spacingAndGlyphs">PERSONALENTWICKLUNG</text>
    <text class="topic" x="502" y="566" font-size="35" text-anchor="end" textLength="346" lengthAdjust="spacingAndGlyphs">PERSONALFÜHRUNG</text>

    <!-- leaders -->
    <polyline class="leader" points="506,420 716,420 716,462"/>
    <polyline class="leader" points="506,491 609,491 609,645"/>
    <polyline class="leader" points="506,566 549,566 549,777"/>

    <!-- rising bars -->
    <rect x="545" y="773" width="44" height="73" fill="url(#cloud-fill)" role="img" aria-label="Wolkenhimmel-Illustration, kleiner Balken"/>
    <rect x="605" y="643" width="90" height="203" fill="url(#cloud-fill)" role="img" aria-label="Wolkenhimmel-Illustration, mittlerer Balken"/>
    <rect x="712" y="460" width="136" height="386" fill="url(#cloud-fill)" role="img" aria-label="Wolkenhimmel-Illustration, großer Balken"/>

    <!-- brand -->
    <text class="brand-name" x="989" y="112" font-size="31" text-anchor="middle" textLength="244" lengthAdjust="spacingAndGlyphs">NORWALDT</text>
    <text class="brand-name" x="989" y="127" font-size="12" text-anchor="middle" letter-spacing="2">COACHING</text>

    <!-- image column -->
    <rect x="867" y="149" width="244" height="133" fill="url(#city-fill)" role="img" aria-label="Illustration: Geschäftsleute im Startblock vor einer Stadtsilhouette"/>
    <rect x="867" y="283" width="244" height="563" fill="url(#column-fill)" role="img" aria-label="Illustrationen: Sprung über ein Balkendiagramm, Team mit Führungskraft, Menschen auf verschlungenen Wegen"/>
  </svg>
</main>
</body>
</html>
```